BRIXLEY ELECTRICAL

all black background with silver and lime writing, fonts i like are gothic style but am open to ideas, will need a picture logo aswell as im putting this on my van.i am a electrical contractor starting up my own electrical business. underneath brixley electrical heading on card we could put" professiona cost effective soloutions to all your electrical needs".{ or something of that nature }.on aback of card on top half list servises provided, real estate and commercial maintenance, new home and renovation rewires and upgrades, split system air conditioning, floor heat, tv phone data, smoke detoctors, lighting systems , builders welcome, , and also a thankyou for your business.

Industry/Entity Type

Real Estate

Contact Information for Business Card

GAVIN PRESTWORTH
brixleyelectrical@quillnet.com.au
0417352940
lic no 81926
ac lic no l593721
abn 37216405813

```html
<!DOCTYPE html>
<html lang="en">
<head>
<meta charset="utf-8">
<title>Brixley Electrical – Business Card</title>
<link href="https://fonts.googleapis.com/css2?family=Jost:ital,wght@0,400;0,600;0,700;1,400&display=swap" rel="stylesheet">
<style>
  :root {
    --page: #ffffff;
    --card: #000000;
    --lime: #8cc63f;
    --silver: #c8c8c8;
    --text: #d9d9d9;
    --shadow: rgba(0,0,0,0.45);
  }
  * { margin: 0; padding: 0; box-sizing: border-box; }
  html, body { width: 1200px; height: 1000px; overflow: hidden; background: var(--page); }
  body { position: relative; font-family: "Jost", "Century Gothic", sans-serif; color: var(--text); }

  .card {
    position: absolute;
    width: 717px;
    height: 443px;
    background: var(--card);
    box-shadow: 4px 5px 8px var(--shadow);
  }
  .card--front { left: 359px; top: 42px; }
  .card--back { left: 124px; top: 517px; }

  .wordmark {
    position: absolute;
    color: var(--lime);
    font-weight: 700;
    white-space: nowrap;
    letter-spacing: 1px;
  }
  .tagline {
    position: absolute;
    font-style: italic;
    color: var(--silver);
    white-space: nowrap;
  }
  .card--front .wordmark { left: 54px; top: 66px; font-size: 52px; line-height: 60px; }
  .card--front .tagline { left: 97px; top: 120px; font-size: 15.5px; }
  .card--back .wordmark { left: 41px; top: 44px; font-size: 35px; line-height: 42px; }
  .card--back .tagline { left: 70px; top: 83px; font-size: 10.5px; }

  .divider { position: absolute; left: 0; width: 100%; }
  .divider__line { position: absolute; left: 0; width: 100%; height: 3px; top: 0; background: var(--silver); }
  .divider__band { position: absolute; left: 0; width: 100%; height: 15px; top: 7px; background: var(--silver); }
  .card--front .divider { top: 164px; }
  .card--back .divider { top: 164px; }

  .holder-name {
    position: absolute;
    left: 336px; top: 213px;
    font-size: 23px; font-weight: 600;
    letter-spacing: 0.5px;
    color: var(--lime);
  }
  .contact-list { position: absolute; left: 336px; top: 275px; list-style: none; font-size: 16px; }
  .contact-list li { height: 27px; line-height: 22px; display: flex; align-items: center; gap: 6px; }
  .contact-list svg { width: 20px; height: 14px; fill: var(--lime); }
  .contact-label { color: var(--lime); }

  .services-title {
    position: absolute; left: 41px; top: 136px;
    font-size: 20px; color: var(--lime); letter-spacing: 0.5px;
  }
  .services-list { position: absolute; left: 42px; top: 205px; list-style: none; font-size: 16.5px; }
  .services-list li { height: 24px; line-height: 24px; display: flex; align-items: center; gap: 3px; }
  .services-list svg { width: 9px; height: 10px; fill: var(--lime); }
  .closing { position: absolute; left: 41px; top: 374px; font-size: 16.5px; }
</style>
</head>
<body>

<section class="card card--front">
  <div class="wordmark">BRIXLEY ELECTRICAL</div>
  <div class="tagline">professionaL cost effective soloutions to all your electrical needs</div>
  <div class="divider"><div class="divider__line"></div><div class="divider__band"></div></div>

  <h1 class="holder-name">GAVIN PRESTWORTH</h1>
  <ul class="contact-list">
    <li><svg viewBox="0 0 20 14" aria-hidden="true"><path d="M2 5c0-3 16-3 16 0l-1 2h-3l-1-2H7L6 7H3z"/><path d="M5 8h10l2 5H3z"/></svg>0417352940</li>
    <li><svg viewBox="0 0 20 14" aria-hidden="true"><path d="M1 1h18v12H1z M2 2l8 6 8-6" stroke="#000" stroke-width="1.2"/></svg>brixleyelectrical@quillnet.com.au</li>
    <li><span class="contact-label">lic no</span> 81926</li>
    <li><span class="contact-label">ac lic no</span> l593721</li>
    <li><span class="contact-label">abn</span> 37216405813</li>
  </ul>
</section>

<section class="card card--back">
  <div class="wordmark">BRIXLEY ELECTRICAL</div>
  <div class="tagline">professionaL cost effective soloutions to all your electrical needs</div>
  <h2 class="services-title">SERVICES PROVIDED:</h2>
  <div class="divider"><div class="divider__line"></div><div class="divider__band"></div></div>

  <ul class="services-list">
    <li><svg viewBox="0 0 9 10" aria-hidden="true"><path d="M0 0l9 5-9 5z"/></svg>real estate and commercial maintenance</li>
    <li><svg viewBox="0 0 9 10" aria-hidden="true"><path d="M0 0l9 5-9 5z"/></svg>new home and renovation rewires and upgrades</li>
    <li><svg viewBox="0 0 9 10" aria-hidden="true"><path d="M0 0l9 5-9 5z"/></svg>split system air conditioning</li>
    <li><svg viewBox="0 0 9 10" aria-hidden="true"><path d="M0 0l9 5-9 5z"/></svg>floor heat</li>
    <li><svg viewBox="0 0 9 10" aria-hidden="true"><path d="M0 0l9 5-9 5z"/></svg>tv phone data</li>
    <li><svg viewBox="0 0 9 10" aria-hidden="true"><path d="M0 0l9 5-9 5z"/></svg>smoke detectors</li>
    <li><svg viewBox="0 0 9 10" aria-hidden="true"><path d="M0 0l9 5-9 5z"/></svg>lighting systems</li>
  </ul>
  <p class="closing">builders welcome, , thankyou for your business</p>
</section>

</body>
</html>
```